I need a business card design for my new clinic (SPORTS MEDICINE OF KNEE). I am orthopedist, expert in sports surgery, especially knee surgery. I prefer, as colors, the colors of my logo (green, black and white). I already have my logo and should appear on my card. It's good to see my site to have ideas (www.drlucianovarela.com)
It needs contain:
my name: Dr. Luciano Varela
my registration: CRM 584-902
my specialty: Cirurgia do Joelho / Esporte
my address: Centro Executivo - Pinheiral Plaza
Av. Doutor Augusto Brandão Cunha, 2740 sala 0836
Jd. Ipanema - Ribeirão Preto - SP
my phone number: Tel (16) 8245-3908
my clinic phone: (16) 3670-4851
my e-mail: drlucianovarela@mailbox-exemplo.com
my site: www.drlucianovarela.com

Target Market(s)

futures patients

Industry/Entity Type

Clinic

Requirements
Nice to have
• letters not overfilled
straight lines, with few curves

```html
<!DOCTYPE html>
<html lang="pt-BR">
<head>
<meta charset="utf-8">
<title>Varela Traumatologia Esportiva – Cartão de Visita</title>
<link rel="stylesheet" href="https://fonts.googleapis.com/css2?family=Tinos:wght@400;700&family=Arimo:wght@400;700&display=swap">
<style>
  :root{
    --page-bg:#e9e7e2;
    --green-deep:#164f30;
    --green-mid:#2f8a55;
    --green-light:#58ad79;
    --white:#ffffff;
    --white-soft:rgba(255,255,255,.82);
    --white-line:rgba(255,255,255,.7);
    --mark-dark:#2b2b2b;
  }
  *{margin:0;padding:0;box-sizing:border-box}
  html,body{width:1200px;height:1000px;overflow:hidden;background:var(--page-bg)}
  .sheet{position:relative;width:1200px;height:1000px}
  .card{
    position:absolute;left:170px;width:860px;height:460px;overflow:hidden;
    background:var(--green-mid);
    box-shadow:0 10px 28px rgba(0,0,0,.25);
  }
  .card--front{top:20px}
  .card--back{top:520px}
  .card__backdrop{
    position:absolute;inset:0;
    background:linear-gradient(160deg,var(--green-deep) 0%,var(--green-mid) 50%,var(--green-light) 100%);
  }
  .brand{position:absolute;display:flex;align-items:center;gap:18px;color:var(--white)}
  .brand__square{flex:0 0 auto;width:62px;height:62px;border-radius:8px;background:var(--mark-dark);border:3px solid var(--white)}
  .brand__name{font-family:"Tinos",serif;font-weight:700;font-size:64px;line-height:1;letter-spacing:2px;color:var(--white)}
  .brand__tagline{font-family:"Tinos",serif;font-weight:400;font-size:20px;color:var(--white-soft);margin-top:4px;letter-spacing:.5px}
  .card--front .brand{left:250px;top:190px}
  .card--back .brand{left:60px;top:300px}
  .card--back .brand__square{width:48px;height:48px}
  .card--back .brand__name{font-size:48px}
  .card--back .brand__tagline{font-size:16px}
  .divider{position:absolute;left:380px;top:50px;width:1px;height:360px;background:var(--white-line)}
  .contact{position:absolute;left:415px;top:55px;right:30px;color:var(--white);font-family:"Arimo",sans-serif}
  .contact__name{font-family:"Tinos",serif;font-weight:700;font-size:30px;line-height:1.2;margin-bottom:6px}
  .contact__specialty,.contact__crm{font-weight:700;font-size:16px;line-height:1.4}
  .contact__list{list-style:none;margin-top:26px}
  .contact__item{display:flex;align-items:flex-start;gap:12px;font-size:14px;line-height:1.45;margin-bottom:12px}
  .contact__icon{flex:0 0 18px;width:18px;height:18px;margin-top:1px}
</style>
</head>
<body>
<main class="sheet">

  <section class="card card--front" aria-label="Frente do cartão">
    <div class="card__backdrop" role="img" aria-label="Fundo decorativo em tons de verde"></div>
    <div class="brand">
      <span class="brand__square"></span>
      <div>
        <div class="brand__name">VARELA</div>
        <div class="brand__tagline">Traumatologia Esportiva</div>
      </div>
    </div>
  </section>

  <section class="card card--back" aria-label="Verso do cartão">
    <div class="card__backdrop" role="img" aria-label="Fundo decorativo em tons de verde"></div>

    <div class="brand">
      <span class="brand__square"></span>
      <div>
        <div class="brand__name">VARELA</div>
        <div class="brand__tagline">Traumatologia Esportiva</div>
      </div>
    </div>

    <div class="divider"></div>

    <div class="contact">
      <div class="contact__name">Dr. Luciano Varela</div>
      <div class="contact__specialty">Cirurgia do Joelho / Esporte</div>
      <div class="contact__crm">CRM 584-902</div>
      <ul class="contact__list">
        <li class="contact__item">
          <svg class="contact__icon" viewBox="0 0 18 18" aria-hidden="true"><circle cx="9" cy="9" r="8" fill="none" stroke="#fff" stroke-width="1.4"/><path d="M6 5.5 L7.5 5 L8.3 7 L7.4 7.8 C7.9 9 8.8 9.9 10 10.5 L10.8 9.6 L12.8 10.4 L12.4 12 C9 12.2 5.8 9 6 5.5 Z" fill="#fff"/></svg>
          <span>Tel (16) 8245-3908 &nbsp;|&nbsp; (16) 3670-4851</span>
        </li>
        <li class="contact__item">
          <svg class="contact__icon" viewBox="0 0 18 18" aria-hidden="true"><rect x="1.5" y="4" width="15" height="10" fill="none" stroke="#fff" stroke-width="1.4"/><path d="M1.5 4 L9 10 L16.5 4" fill="none" stroke="#fff" stroke-width="1.4"/></svg>
          <span>drlucianovarela@mailbox-exemplo.com</span>
        </li>
        <li class="contact__item">
          <svg class="contact__icon" viewBox="0 0 18 18" aria-hidden="true"><circle cx="9" cy="9" r="7.5" fill="none" stroke="#fff" stroke-width="1.4"/><ellipse cx="9" cy="9" rx="3.2" ry="7.5" fill="none" stroke="#fff" stroke-width="1.2"/><path d="M1.5 9 H16.5" stroke="#fff" stroke-width="1.2"/></svg>
          <span>www.drlucianovarela.com</span>
        </li>
        <li class="contact__item">
          <svg class="contact__icon" viewBox="0 0 18 18" aria-hidden="true"><path d="M9 17 C9 17 3 10.5 3 7 A6 6 0 0 1 15 7 C15 10.5 9 17 9 17 Z" fill="#fff"/><circle cx="9" cy="7" r="2.2" fill="#2f8a55"/></svg>
          <span>Centro Executivo - Pinheiral Plaza<br>Av. Doutor Augusto Brandão Cunha, 2740 sala 0836<br>Jd. Ipanema - Ribeirão Preto - SP</span>
        </li>
      </ul>
    </div>
  </section>

</main>
</body>
</html>
```